Psychotherapist need a business card with logo

I am a psychotherapist in need of a business card. The card must have:

Marisol Trevuneda
Psicoterapeuta
937 281 706

Psychologists use the greek letter psy, which is the psychologist symbol, but I would prefer something like a mandala, a graphic symbol, an iconic tree, nothing very usual, but something that shows confidence and trust.

Industry/Entity Type

Business

```html
<!DOCTYPE html>
<html lang="es">
<head>
<meta charset="utf-8">
<title>Marisol Trevuneda – Psicoterapeuta</title>
<link rel="stylesheet" href="https://fonts.googleapis.com/css2?family=Dosis:wght@500;600&display=swap">
<style>
  :root {
    --backdrop: #e6e3df;
    --card-dark: #272727;
    --card-mid: #333333;
    --ink-light: #cfcfcf;
    --ink-bright: #f2f2f2;
    --rule: #8a8a8a;
  }
  * { margin: 0; padding: 0; box-sizing: border-box; }
  html, body {
    width: 1200px;
    height: 735px;
    overflow: hidden;
    background: var(--backdrop);
  }
  .business-card {
    position: absolute;
    left: 100px;
    top: 82px;
    width: 1000px;
    height: 571px;
    background: linear-gradient(160deg, var(--card-mid) 0%, var(--card-dark) 100%);
    border-radius: 6px;
    box-shadow: 0 14px 30px rgba(0, 0, 0, 0.25);
    font-family: "Dosis", "Arial Narrow", sans-serif;
    color: var(--ink-light);
  }
  .brand-mark {
    position: absolute;
    left: 0;
    right: 0;
    top: 140px;
    display: flex;
    justify-content: center;
    align-items: center;
    gap: 22px;
  }
  .brand-mark__dot {
    width: 40px;
    height: 40px;
    border-radius: 50%;
    background: var(--ink-bright);
  }
  .brand-mark__name {
    font-size: 64px;
    font-weight: 600;
    letter-spacing: 2px;
    color: var(--ink-bright);
    line-height: 1;
  }
  .identity-line {
    position: absolute;
    left: 80px;
    right: 60px;
    top: 298px;
    text-align: right;
    font-size: 44px;
    font-weight: 500;
    letter-spacing: 1px;
    white-space: nowrap;
  }
  .divider {
    position: absolute;
    left: 0;
    right: 0;
    height: 2px;
    background: var(--rule);
    opacity: 0.7;
  }
  .divider--upper { top: 366px; }
  .divider--lower { top: 476px; }
  .contact-row {
    position: absolute;
    left: 0;
    right: 0;
    top: 394px;
    display: flex;
    justify-content: center;
    align-items: center;
    gap: 22px;
  }
  .contact-row__icon { width: 50px; height: 50px; }
  .contact-row__phone {
    font-size: 44px;
    font-weight: 600;
    letter-spacing: 1px;
    color: var(--ink-bright);
  }
</style>
</head>
<body>
  <div class="business-card">
    <div class="brand-mark">
      <span class="brand-mark__dot"></span>
      <span class="brand-mark__name">Trevuneda</span>
    </div>

    <p class="identity-line">Marisol Trevuneda – Psicoterapeuta</p>

    <div class="divider divider--upper"></div>

    <div class="contact-row">
      <svg class="contact-row__icon" viewBox="0 0 50 50" aria-hidden="true">
        <circle cx="25" cy="25" r="23" fill="none" stroke="#cfcfcf" stroke-width="2"/>
        <rect x="18" y="12" width="14" height="26" rx="2.5" fill="none" stroke="#cfcfcf" stroke-width="2"/>
        <line x1="18" y1="16.5" x2="32" y2="16.5" stroke="#cfcfcf" stroke-width="1.5"/>
        <line x1="18" y1="32.5" x2="32" y2="32.5" stroke="#cfcfcf" stroke-width="1.5"/>
        <circle cx="25" cy="35.3" r="1.3" fill="#cfcfcf"/>
      </svg>
      <span class="contact-row__phone">937 281 706</span>
    </div>

    <div class="divider divider--lower"></div>
  </div>
</body>
</html>
```